Cosmetic Surgery Monthly Newsletter

- A4 fold out dm flyer (2up on A3, duplex)
- Refer to website for look and feel http://drpemberton.com.au Looking for a fresh, medical look with a corporate feel newsletter.
- Layout that can have different body of text dropped into it on different topics. These topics will also have images that will go with the relevent copy to demonstrate some of the cosmetic work being done.
Headings to have nice fresh look and feel, with body text to have light translucent colour behind text to make it look nice.
Need to incorporate social media logos - like us on Facebook, twiiter, LinkedIn, Youtube.

Target Market(s)

Target market is high end market aged anywhere between 20-50+ This cosmetic surgery is situated in a prestigous location and therefore its clients are willing to pay for Dr Pembertons many years of experience. He is highly qualified and has an excellent reputation.

Industry/Entity Type

Medical

Font styles to use
Serif

Requirements
Must have
• must be in line with the website look and feel
• Logo to come
Should not have
• large solid black areas

```html
<!DOCTYPE html>
<html lang="en">
<head>
<meta charset="utf-8">
<title>Dr Pemberton – Newsletter Spread</title>
<link href="https://fonts.googleapis.com/css2?family=Marcellus&family=Arimo:wght@400;700&family=Roboto+Condensed:wght@400&display=swap" rel="stylesheet">
<style>
  :root{
    --bg:#e9e6e2;
    --paper:#ffffff;
    --paper-shade:#f1f1f1;
    --brand-red:#8e1f1c;
    --ink:#2b2b2b;
    --ink-soft:#3a3a3a;
    --salmon:#f39a84;
    --photo-skin:#d9b29c;
    --photo-blue:#5f6f86;
  }
  *{box-sizing:border-box;margin:0;padding:0}
  html,body{width:1200px;height:963px;overflow:hidden;background:var(--bg)}
  .spread{position:absolute;left:40px;top:42px;width:1120px;height:880px;background:linear-gradient(90deg,var(--paper) 0,var(--paper-shade) 49.4%,#dcdcdc 50%,var(--paper) 50.8%,var(--paper) 100%);box-shadow:0 6px 18px rgba(0,0,0,.18);overflow:hidden;font-family:"Arimo",Arial,sans-serif;color:var(--ink)}
  .ph{position:absolute;display:block}
  .serif-title{font-family:"Marcellus",serif;color:var(--brand-red);font-weight:400}

  /* left page */
  .doctor-name{position:absolute;left:36px;top:34px;font-size:31px;letter-spacing:.3px}
  .portrait{left:36px;top:86px;width:204px;height:200px;background:linear-gradient(90deg,#b39582 0,#8c7060 30%,#2d2c3a 45%,#2b2a36 70%,#6d5a55 100%)}
  .body-copy{position:absolute;font-size:15px;line-height:19px;text-align:justify}
  .quote{left:252px;top:86px;width:290px;text-indent:12px}
  .quote .sign{display:block;text-align:right;padding-right:12px}
  .bio{left:252px;top:200px;width:290px;text-indent:40px}
  .charity{left:36px;top:296px;width:506px;text-indent:34px}
  .result-photo{top:456px;height:136px;background:linear-gradient(170deg,#cfa895,#9b6e5e 60%,var(--photo-blue))}
  .caption{position:absolute;top:604px;font-size:14.5px;line-height:19px;color:var(--brand-red)}

  /* right page */
  .procedures-title{position:absolute;left:598px;top:22px;font-size:24px;line-height:36px;letter-spacing:.3px}
  .group-title{position:absolute;font-size:23px;color:var(--brand-red);font-weight:400}
  .group-list{position:absolute;font-family:"Roboto Condensed","Arial Narrow",sans-serif;font-size:14px;line-height:18px;color:var(--ink-soft);text-transform:uppercase;white-space:nowrap}
  .proc-photo{background:linear-gradient(160deg,#f3dccd,var(--photo-skin) 55%,#b98670);border:3px solid #fff;box-shadow:0 1px 4px rgba(0,0,0,.2)}

  /* band */
  .band{position:absolute;left:0;top:0}
  .brand-dot{position:absolute;left:96px;top:752px;width:34px;height:34px;border-radius:50%;background:var(--ink)}
  .brand-name{position:absolute;left:150px;top:746px;font-size:34px;letter-spacing:5px;color:var(--ink)}
  .brand-line{position:absolute;left:153px;top:792px;font-size:11.5px;letter-spacing:7px;color:var(--ink)}
  .tagline{position:absolute;left:590px;top:716px;width:500px;font-size:22px;line-height:30px;color:#111;text-align:center}
</style>
</head>
<body>
<main class="spread">
  <svg class="band" width="1120" height="880" viewBox="0 0 1120 880" aria-hidden="true">
    <defs>
      <linearGradient id="bandFill" x1="0" y1="0" x2="0" y2="1">
        <stop offset="0" stop-color="#f6ad98"/>
        <stop offset="1" stop-color="#f08d76"/>
      </linearGradient>
    </defs>
    <path d="M0,570 C220,640 470,730 660,722 C840,714 1000,640 1120,600 L1120,880 L0,880 Z" fill="#f8d3c7"/>
    <path d="M0,592 C220,664 470,748 660,740 C840,732 1000,662 1120,622 L1120,880 L0,880 Z" fill="#fbe6df"/>
    <path d="M0,612 C220,690 470,770 660,762 C840,754 1000,684 1120,644 L1120,880 L0,880 Z" fill="url(#bandFill)"/>
    <path d="M0,632 C220,710 470,782 660,776 C840,770 1000,706 1120,668" fill="none" stroke="#fbd0c3" stroke-width="2"/>
  </svg>

  <!-- left page -->
  <h1 class="doctor-name serif-title">DR. GRAHAM PEMBERTON</h1>
  <div class="ph portrait" role="img" aria-label="Portrait photo of the surgeon in a dark suit"></div>
  <p class="body-copy quote">“From straightening a less than perfect nose to smoothing the scars of birth defects, this medical specialty deals with more than bones and tissue, it can heal a patient’s damaged self-esteem.”<span class="sign">- Dr. Pemberton</span></p>
  <p class="body-copy bio">Dr. Graham J. Pemberton is recognized world-wide as an expert in cosmetic plastic surgery with more than thirty years of experience in both cosmetic and plastic/reconstructive surgery.</p>
  <p class="body-copy charity">Dr. Pemberton is also the Founder and a Director of Project Bright Smile Australia. This Australian based charity draws on the talents of medical professionals from all over the world to educate medical professionals and care for children in the Philippines with cleft lip and palate. Project Bright Smile has now provided cleft lip and palate surgery to nearly 3,000 children and other medical services to many, many more whom without charity would have gone unaided.</p>

  <div class="ph result-photo" style="left:44px;width:112px" role="img" aria-label="Before photo of facelift patient"></div>
  <div class="ph result-photo" style="left:172px;width:112px" role="img" aria-label="After photo of facelift patient"></div>
  <div class="ph result-photo" style="left:320px;width:112px" role="img" aria-label="Before photo of rhinoplasty patient"></div>
  <div class="ph result-photo" style="left:434px;width:112px" role="img" aria-label="After photo of rhinoplasty patient"></div>
  <p class="caption" style="left:46px;width:250px">Before and 6 months after Facelift and Necklift</p>
  <p class="caption" style="left:322px;width:190px">Before and 6 months after Ethnic Rhinoplasty</p>

  <!-- right page -->
  <h2 class="procedures-title serif-title">PROCEDURES WE OFFER -<br>SEE WHAT WE CAN DO FOR YOU</h2>

  <div class="ph proc-photo" style="left:600px;top:118px;width:96px;height:118px" role="img" aria-label="Photo of a woman's face"></div>
  <h3 class="group-title" style="left:708px;top:110px">Face</h3>
  <p class="group-list" style="left:708px;top:142px">Facelifts, browlift, eyelid surgery, nose reshaping,<br>cheek implants, chin implants, neck liposuction,<br>laserbrasion / dermabrasion, lip augmentation,<br>ear reshaping</p>

  <h3 class="group-title" style="left:604px;top:254px">Breast</h3>
  <p class="group-list" style="left:606px;top:288px">Breast implants, breast lifting, breast reduction<br>breast reconstruction, inverted nipples</p>
  <div class="ph proc-photo" style="left:962px;top:212px;width:118px;height:128px" role="img" aria-label="Photo of a woman's torso"></div>

  <div class="ph proc-photo" style="left:610px;top:352px;width:92px;height:118px" role="img" aria-label="Photo of a man's torso"></div>
  <h3 class="group-title" style="left:716px;top:350px">Body</h3>
  <p class="group-list" style="left:718px;top:382px">Liposuction / liposculpture, tummy tucks<br>gynecomastia (man boobs), pectoral implants<br>calf implants, buttock implants,<br>custom body implants, arm lifts</p>

  <div class="ph proc-photo" style="left:978px;top:438px;width:110px;height:128px" role="img" aria-label="Photo of a woman touching her cheek"></div>
  <h3 class="group-title" style="left:610px;top:482px">Non-Surgical</h3>
  <p class="group-list" style="left:612px;top:516px">Radiance RF, anti-wrinkle injections, injectible fillers<br>laser for facial veins, skin peels,<br>microdermabrasion</p>

  <div class="ph proc-photo" style="left:618px;top:588px;width:100px;height:118px" role="img" aria-label="Photo of a woman's face with skin highlight"></div>
  <h3 class="group-title" style="left:736px;top:588px">Restorative</h3>
  <p class="group-list" style="left:738px;top:620px">Skin cancer surgery<br>breast reconstruction<br>cleft lip &amp; palate</p>

  <!-- band content -->
  <span class="brand-dot" aria-hidden="true"></span>
  <p class="brand-name">DR PEMBERTON</p>
  <p class="brand-line">COSMETIC PLASTIC SURGEON</p>
  <p class="tagline">The Pre-eminent authority in Sydney Cosmetic Plastic Surgery. Over 30 years of quallity results.</p>
</main>
</body>
</html>
```